Sketch Harbor Business Card

I have attached several examples of business cards that I have seen online that I liked. We will be incorporating Spot UV coating and raised ink on the cards. Optionally we may use embossing with color. The business card will be used for 3d printing services. We are hoping to see some different color options of cards (i.e. black card, white card, etc.). We look forward to your ideas.

Industry/Entity Type

Printing

Requirements
Must have
• Dorian Makk
Founder and CEO
+1.555.010.2231 cell
+1.555.010.4786 office
+1.555.010.4786 fax
Dorian.Makk@3dKestrelo.com
www.3dKestrelo.com
Nice to have
• I would be nice to see some 3d background designs to add some depth to the designs of the cards since it is a 3d design company. There are examples of this in the files I have attached.

```html
<!DOCTYPE html>
<html lang="en">
<head>
<meta charset="utf-8">
<title>Kestrelo Business Card</title>
<link rel="stylesheet" href="https://fonts.googleapis.com/css2?family=Rokkitt:wght@400;500&family=Raleway:wght@400&display=swap">
<style>
  :root {
    --page: #ffffff;
    --card-top: #3b3b3b;
    --card-top-deep: #343434;
    --texture-light: #4a4a4a;
    --texture-dark: #2f2f2f;
    --accent-blue: #1f9ad6;
    --accent-pink: #e5338c;
    --panel: #ffffff;
    --panel-edge: #ececec;
    --ink: #3a3a3a;
    --icon-well: #3d3d3d;
  }
  * { margin: 0; padding: 0; box-sizing: border-box; }
  html, body { width: 1200px; height: 686px; overflow: hidden; background: var(--page); }
  .card {
    position: relative;
    width: 1200px;
    height: 686px;
    border-radius: 28px;
    overflow: hidden;
    background: var(--card-top);
    font-family: "Rokkitt", Georgia, serif;
  }
  .card__top {
    position: absolute; left: 0; top: 0; width: 100%; height: 316px;
    background: linear-gradient(180deg, var(--card-top) 0%, var(--card-top-deep) 100%);
  }
  .card__rule {
    position: absolute; left: 0; top: 316px; width: 100%; height: 10px;
    background: var(--accent-blue);
  }
  .card__texture {
    position: absolute; left: 0; top: 326px; width: 100%; height: 360px;
    background: radial-gradient(ellipse at 30% 30%, var(--texture-light) 0%, var(--texture-dark) 85%);
  }
  .identity { position: absolute; left: 153px; top: 98px; }
  .identity__name {
    font-size: 56px; font-weight: 400; color: var(--accent-pink); line-height: 1;
  }
  .identity__role {
    position: absolute; left: 60px; top: 84px; white-space: nowrap;
    font-size: 33px; font-weight: 500; color: var(--accent-blue); line-height: 1;
  }
  .contact-icons {
    position: absolute; left: 103px; top: 366px; width: 62px; height: 270px;
    border-radius: 14px; background: var(--icon-well);
  }
  .contact-list { position: absolute; left: 103px; top: 380px; list-style: none; }
  .contact-list li {
    display: flex; align-items: center; height: 46px;
    font-size: 34px; color: var(--accent-blue); line-height: 1;
  }
  .contact-list li.gap { margin-top: 18px; }
  .contact-list svg { width: 62px; height: 34px; flex: none; margin-right: 18px; }
  .brand-panel {
    position: absolute; left: 722px; top: 155px; width: 478px; height: 375px;
    background: linear-gradient(135deg, var(--panel) 60%, var(--panel-edge) 100%);
    border-radius: 28px 0 0 28px;
    box-shadow: -6px 8px 18px rgba(0,0,0,0.55);
  }
  .brand-panel__dot {
    position: absolute; left: 168px; top: 42px; width: 142px; height: 142px;
    border-radius: 50%; background: var(--ink);
  }
  .brand-panel__name {
    position: absolute; left: 0; width: 100%; top: 248px; text-align: center;
    font-family: "Rokkitt", Georgia, serif; font-weight: 400;
    font-size: 52px; letter-spacing: 12px; color: var(--ink); line-height: 1;
    padding-left: 12px;
  }
  .brand-panel__tagline {
    position: absolute; left: 0; width: 100%; top: 312px; text-align: center;
    font-size: 31px; letter-spacing: 3px; color: var(--accent-pink); line-height: 1;
  }
</style>
</head>
<body>
  <div class="card">
    <div class="card__top"></div>
    <div class="card__rule"></div>
    <div class="card__texture" role="img" aria-label="Fine dark crosshatch texture across the lower half of the card"></div>

    <div class="identity">
      <h1 class="identity__name">Dorian Makk</h1>
      <p class="identity__role">Founder &amp; CEO</p>
    </div>

    <div class="contact-icons"></div>
    <ul class="contact-list">
      <li>
        <svg viewBox="0 0 62 34" aria-hidden="true"><rect x="23" y="4" width="16" height="26" rx="3" fill="none" stroke="var(--accent-blue)" stroke-width="2.5"/><circle cx="31" cy="25" r="1.8" fill="var(--accent-blue)"/></svg>
        +1.555.010.2231
      </li>
      <li>
        <svg viewBox="0 0 62 34" aria-hidden="true"><path d="M18 12 q13 -9 26 0 v4 h-6 v-3 h-14 v3 h-6z" fill="var(--accent-blue)"/><rect x="20" y="18" width="22" height="12" rx="2" fill="var(--accent-blue)"/></svg>
        +1.555.010.4786
      </li>
      <li>
        <svg viewBox="0 0 62 34" aria-hidden="true"><rect x="24" y="3" width="14" height="10" fill="none" stroke="var(--accent-blue)" stroke-width="2.5"/><rect x="18" y="13" width="26" height="17" rx="2" fill="var(--accent-blue)"/></svg>
        +1.555.010.4786
      </li>
      <li class="gap">
        <svg viewBox="0 0 62 34" aria-hidden="true"><rect x="18" y="7" width="26" height="20" fill="none" stroke="var(--accent-blue)" stroke-width="2.5"/><path d="M18 7 l13 11 l13 -11" fill="none" stroke="var(--accent-blue)" stroke-width="2.5"/></svg>
        Dorian.Makk@3dKestrelo.com
      </li>
      <li>
        <svg viewBox="0 0 62 34" aria-hidden="true"><circle cx="31" cy="17" r="13" fill="var(--accent-blue)"/><path d="M31 4 v26 M18 17 h26 M22 8 q9 9 0 18 M40 8 q-9 9 0 18" fill="none" stroke="var(--icon-well)" stroke-width="1.8"/></svg>
        www.3dKestrelo.com
      </li>
    </ul>

    <div class="brand-panel">
      <div class="brand-panel__dot"></div>
      <p class="brand-panel__name">KESTRELO</p>
      <p class="brand-panel__tagline">Design Studio</p>
    </div>
  </div>
</body>
</html>
```